Dating Coach needs a Book Cover Design

My new book called "When to Turn the Tide: Meeting Romance Among the Endless Crowd of Digital Courtship" needs a cover! I tried to make one on my own, but it's just not my skill set :) Please see attached for my best attempt. I'd like to see the title smaller and the tagline bigger - so that the tagline is easier to read. But I'm not sure how to do this and still have the Title look great. I'm also considering if the "TURN THE TIDE" part should not be in all caps. Looking forward to your ideas! I'm also afraid that the drawing is a bit too cartoonish and doesn't match my brand. I'm looking for something elegant and also very approachable and down to earth. My website is www.petrawendtcoaching.example so you can use as reference! Please see my attached brand style guide for colors. This will be an e-book that I give away for free to anyone who signs up for my newsletter. Some mock-ups would also be great to use in advertising.

```html
<!DOCTYPE html>
<html lang="en">
<head>
<meta charset="utf-8">
<title>When to Turn the Tide — Book Cover</title>
<link rel="stylesheet" href="https://fonts.googleapis.com/css2?family=Cormorant+Garamond:wght@500;600&family=Gilda+Display&display=swap">
<style>
  :root {
    --page-bg: #ece8e2;
    --cover-cream: #f6f0e6;
    --cover-glow: #fbf8f2;
    --plum: #6f4f86;
    --olive: #6b5a2c;
    --gold-line: #a88f55;
    --straw-light: #dcc08c;
    --straw-mid: #c4a068;
  }
  * { margin: 0; padding: 0; box-sizing: border-box; }
  html, body {
    width: 1200px; height: 1200px; overflow: hidden;
    background: var(--page-bg);
  }
  .book-cover {
    position: absolute;
    left: 240px; top: 50px;
    width: 720px; height: 1100px;
    overflow: hidden;
    background: radial-gradient(ellipse at 50% 30%, var(--cover-glow) 0%, var(--cover-cream) 60%, #efe5d4 100%);
    box-shadow: 0 18px 40px rgba(80, 60, 40, 0.18);
  }
  .cover-artwork {
    position: absolute;
    left: 0; top: 620px;
    width: 720px; height: 440px;
    background: linear-gradient(to bottom, var(--straw-light) 0%, var(--straw-mid) 100%);
    -webkit-mask-image: linear-gradient(to bottom, transparent 0%, #000 22%, #000 72%, transparent 100%);
    mask-image: linear-gradient(to bottom, transparent 0%, #000 22%, #000 72%, transparent 100%);
  }
  .cover-text {
    position: absolute; left: 0; width: 100%;
    text-align: center;
  }
  .title-lead {
    top: 82px;
    font-family: "Cormorant Garamond", serif;
    font-weight: 500;
    font-size: 44px;
    color: var(--plum);
  }
  .title-main {
    top: 187px;
    font-family: "Cormorant Garamond", serif;
    font-weight: 500;
    font-size: 124px;
    line-height: 108px;
    color: var(--plum);
  }
  .title-divider {
    position: absolute; left: 190px; top: 438px;
    width: 340px; height: 30px;
  }
  .subtitle {
    top: 486px;
    font-family: "Gilda Display", serif;
    font-size: 33px;
    line-height: 51px;
    letter-spacing: 2px;
    color: var(--olive);
  }
  .author {
    top: 995px;
    font-family: "Gilda Display", serif;
    font-size: 34px;
    letter-spacing: 5px;
    color: var(--olive);
  }
</style>
</head>
<body>
  <main class="book-cover">
    <div class="cover-artwork" role="img" aria-label="Photograph of golden straw with a lavender heart-shaped stone resting in it"></div>

    <p class="cover-text title-lead">When to</p>
    <h1 class="cover-text title-main">Turn the<br>Tide</h1>

    <svg class="title-divider" viewBox="0 0 340 30" aria-hidden="true">
      <line x1="0" y1="15" x2="150" y2="15" stroke="var(--gold-line)" stroke-width="1.5"/>
      <line x1="190" y1="15" x2="340" y2="15" stroke="var(--gold-line)" stroke-width="1.5"/>
      <path d="M170 24 C160 17 156 12 158 8 C160 4 166 4 170 9 C174 4 180 4 182 8 C184 12 180 17 170 24 Z"
            fill="none" stroke="var(--gold-line)" stroke-width="1.5"/>
    </svg>

    <p class="cover-text subtitle">Meeting Romance Among the<br>Endless Crowd<br>of Digital Courtship</p>

    <p class="cover-text author">PETRA WENDT</p>
  </main>
</body>
</html>
```